Baby Sling

We need packaging designed for our new baby sling. We need it to project a premium product that is high quality, eco-friendly and appeals to Mums and Dads. It must be gender neutral, yet incorporate some of our logo colours of pink and green. Perhaps it could include some neutral colours such as light brown/mocha/latte.
We are happy if the images are 3D rendered.
The essence of our brand is high quality, eco-friendly, natural baby products and we would like this reflected in our packaging design.
Additionally, we need our logo fixed. The wording around the centre image is slightly off and needs to be balanced, should be very easy to do.

Target Market(s)

Mums and Dads with new baby

Industry/Entity Type

Baby

Requirements
Must have
• Our logo, images of sling, features and benefits

```html
<!DOCTYPE html>
<html lang="en">
<head>
<meta charset="utf-8">
<title>Nestwell Baby – Adjustable Baby Sling Packaging</title>
<link rel="stylesheet" href="https://fonts.googleapis.com/css2?family=Roboto+Condensed:wght@400;500;700&display=swap">
<style>
  :root {
    --bg: #ececec;
    --panel-cream: #faf6f1;
    --latte: #d9c3a9;
    --latte-pale: #efe3d5;
    --mocha: #8a6a55;
    --mocha-deep: #5a4236;
    --sage: #8dbf8b;
    --sage-deep: #5f9a63;
    --blush: #e79bb0;
    --blush-pale: #f6d3dc;
    --feature-grey: #6d5f57;
    --white: #ffffff;
  }
  * { margin: 0; padding: 0; box-sizing: border-box; }
  html, body { width: 1200px; height: 1000px; overflow: hidden; }
  body {
    background: var(--bg);
    font-family: "Roboto Condensed", "Arial Narrow", sans-serif;
    position: relative;
  }
  .package {
    position: absolute;
    left: 205px; top: 200px;
    width: 790px; height: 600px;
    display: flex;
    box-shadow: 0 10px 30px rgba(0,0,0,0.12);
  }
  .front-panel {
    position: relative;
    width: 560px; height: 600px;
    background: linear-gradient(180deg, var(--panel-cream) 0%, var(--latte-pale) 100%);
    overflow: hidden;
  }
  .soft-tint {
    position: absolute;
    left: 300px; top: 0; width: 260px; height: 480px;
    background: linear-gradient(200deg, rgba(231,155,176,0.35) 0%, rgba(246,211,220,0.18) 60%, rgba(255,255,255,0) 100%);
  }
  .soft-tint-low {
    position: absolute;
    left: 0; top: 360px; width: 200px; height: 120px;
    background: linear-gradient(90deg, rgba(141,191,139,0.35), rgba(141,191,139,0));
  }
  .brand-tile {
    position: absolute;
    left: 20px; top: 30px;
    width: 180px; height: 180px;
    background: var(--sage);
    border-radius: 0 0 34px 0;
    display: flex; flex-direction: column;
    align-items: center; justify-content: center;
    gap: 14px;
    z-index: 2;
  }
  .brand-mark {
    width: 40px; height: 40px; border-radius: 50%;
    background: var(--white);
  }
  .brand-name {
    color: var(--white);
    font-weight: 700;
    font-size: 28px;
    line-height: 1;
    text-align: center;
  }
  .hero-photo {
    position: absolute;
    left: 150px; top: 75px;
    width: 310px; height: 405px;
    border-radius: 120px 120px 0 0;
    background: linear-gradient(180deg, #4a3d36 0%, #6b5a50 35%, #d9c3a9 65%, #e79bb0 80%, #4a3d36 100%);
  }
  .product-title {
    position: absolute;
    left: 0; top: 480px;
    width: 560px; height: 56px;
    background: var(--mocha-deep);
    color: var(--white);
    font-size: 30px; font-weight: 500;
    letter-spacing: 3px; word-spacing: 10px;
    display: flex; align-items: center; justify-content: center;
  }
  .feature-bar {
    position: absolute;
    left: 0; top: 536px;
    width: 560px; height: 44px;
    background: var(--feature-grey);
    color: var(--white);
    list-style: none;
    display: flex; align-items: center; justify-content: center;
    font-size: 16px; font-weight: 500;
  }
  .feature {
    height: 30px; padding: 0 22px;
    display: flex; align-items: center; justify-content: center;
  }
  .feature + .feature { border-left: 1px solid rgba(255,255,255,0.7); }

  .side-panel {
    width: 230px; height: 600px;
    display: flex;
  }
  .side-heading-strip {
    width: 62px; height: 100%;
    background: var(--mocha);
    position: relative;
  }
  .side-heading {
    position: absolute;
    left: 50%; top: 50%;
    transform: translate(-50%, -50%) rotate(-90deg);
    white-space: nowrap;
    color: var(--white);
    font-size: 32px; font-weight: 500;
    letter-spacing: 2px;
  }
  .positions-column {
    flex: 1;
    background: var(--latte);
    display: flex; flex-direction: column;
    align-items: center; justify-content: center;
    gap: 16px;
  }
  .position-frame {
    width: 136px; height: 124px;
    border: 7px solid var(--blush);
    border-radius: 16px;
    background: var(--white);
    padding: 4px;
  }
  .position-frame:nth-child(even) { border-color: var(--sage-deep); }
  .position-photo {
    width: 100%; height: 100%;
    border-radius: 10px;
    background: linear-gradient(160deg, #efe6dc 0%, #5a4a42 45%, #e79bb0 75%, #e8ddd0 100%);
  }
</style>
</head>
<body>
  <main class="package">
    <section class="front-panel">
      <div class="soft-tint"></div>
      <div class="soft-tint-low"></div>
      <div class="hero-photo" role="img" aria-label="Photo of a parent carrying a baby in the sling"></div>
      <div class="brand-tile">
        <span class="brand-mark"></span>
        <span class="brand-name">Nestwell baby</span>
      </div>
      <h1 class="product-title">ADJUSTABLE BABY SLING</h1>
      <ul class="feature-bar">
        <li class="feature">100% cotton</li>
        <li class="feature">Multiple carrying positions</li>
        <li class="feature">Birth to 16kg</li>
      </ul>
    </section>
    <section class="side-panel">
      <div class="side-heading-strip">
        <h2 class="side-heading">DIFFERENT CARRYING POSITIONS</h2>
      </div>
      <div class="positions-column">
        <div class="position-frame"><div class="position-photo" role="img" aria-label="Photo of a parent wearing the empty sling"></div></div>
        <div class="position-frame"><div class="position-photo" role="img" aria-label="Photo of a baby held upright in the sling"></div></div>
        <div class="position-frame"><div class="position-photo" role="img" aria-label="Photo of a baby cradled lying in the sling"></div></div>
        <div class="position-frame"><div class="position-photo" role="img" aria-label="Photo of a baby sitting on the hip in the sling"></div></div>
      </div>
    </section>
  </main>
</body>
</html>
```